Pondmentor: an app for coaches and students in golf and fitness

I currently have an app that is called Pondmentor and I am redoing the app completely and with this I am looking for a cool design for the app. I am not happy with the design as it is at the moment. The app should have a nice welcome and when you are logged in the dashboard must be very modern. It is a golf app that have 2 type of users. 1 user is the coach and the other user is the student. Those users can see different things of course.
The coach is normally paying a subscription charge for using the app but I want to get the students to pay for different tools that I will be offering via the app. To me the dashboard and the homepage of the app (once you have downloaded the app) is important. Here I would like to get the student as well as the coach the feeling of what the app can offer. The app offers features like Calendar (here the student can book the coach via the calendar), Chat (here the coach and the student can chat with each other as well as the coach can creat group chats with several students), Notes (here the coach as well as the student can create notes for their lessons), video tips (here the coach can upload video tips for his/her students, online lesson (the student can take online lessons by uploading recorded videos..and so on

Target Market(s)

Sport coaches (for start it will be mostly golf coaches)

Industry/Entity Type

Sports

Font styles to use
Sans Serif

Colors
0054AA
0677BA
7BADD7
CADEEF
E8F1F8

Requirements
Must have
• modern design and easy navigation.
Nice to have
• It all starts with the dashboard
Should not have
• boring standard style.

```html
<!DOCTYPE html>
<html lang="en">
<head>
<meta charset="utf-8">
<title>Pondmentor – Coach Dashboard</title>
<link rel="stylesheet" href="https://fonts.googleapis.com/css2?family=Poppins:wght@400;500;600;700&display=swap">
<style>
  :root{
    --navy:#0054AA;
    --blue:#0677BA;
    --sky:#7BADD7;
    --mist:#CADEEF;
    --ice:#E8F1F8;
    --ink:#111a2b;
    --muted:#6b7585;
    --teal-a:#19c2c9;
    --teal-b:#1a8fd8;
    --card-a:#0a47a3;
    --card-b:#2e62d8;
    --pill:#0b3680;
    --white:#ffffff;
  }
  *{box-sizing:border-box;margin:0;padding:0}
  html,body{width:1200px;height:864px;overflow:hidden}
  body{background:var(--ice);font-family:'Poppins',sans-serif;color:var(--ink);position:relative}

  .screen{
    position:absolute;left:444px;top:12px;width:375px;height:1012px;
    transform:scale(0.83);transform-origin:top left;
    background:var(--white);border-radius:30px;overflow:hidden;
    box-shadow:0 20px 60px rgba(0,84,170,.15);
  }
  .abs{position:absolute}

  /* status bar */
  .status-time{left:32px;top:14px;font-size:15px;font-weight:600}
  .status-icons{right:20px;top:16px}

  /* header */
  .avatar{left:20px;top:54px;width:50px;height:50px;border-radius:50%;
    background:radial-gradient(circle at 50% 40%,#d9a27a,#7c5a3c 60%,#3f6d8a)}
  .welcome{left:85px;top:58px;font-size:12.5px;letter-spacing:.3px;color:#4b5363;font-weight:500}
  .coach-name{left:85px;top:76px;font-size:20px;font-weight:700;color:var(--navy)}
  .mail-btn{left:316px;top:60px;width:38px;height:38px;border-radius:50%;background:var(--white);
    box-shadow:0 4px 12px rgba(0,84,170,.18);display:flex;align-items:center;justify-content:center}
  .mail-badge{left:343px;top:54px;width:18px;height:18px;border-radius:50%;background:var(--teal-a);
    color:#fff;font-size:10px;font-weight:600;display:flex;align-items:center;justify-content:center;border:2px solid #fff}

  /* today card */
  .today{left:20px;top:135px;width:335px;height:242px;border-radius:16px;
    background:linear-gradient(135deg,var(--card-a),var(--card-b));box-shadow:0 10px 24px rgba(0,84,170,.3)}
  .today-date{left:20px;top:14px;font-size:12.5px;color:var(--mist);font-weight:500}
  .today-title{left:20px;top:31px;font-size:17px;font-weight:700;color:#fff}
  .view-cal{left:195px;top:19px;width:119px;height:32px;border-radius:16px;background:var(--pill);
    color:#fff;font-size:10.5px;font-weight:600;display:flex;align-items:center;justify-content:center;letter-spacing:.2px}
  .lesson{left:20px;width:294px;height:70px;background:#fff;border-radius:12px;display:flex;align-items:center;padding-left:14px}
  .lesson-icon{width:41px;height:41px;border-radius:50%;background:linear-gradient(135deg,var(--teal-a),var(--teal-b));
    display:flex;align-items:center;justify-content:center;flex:none}
  .lesson-text{margin-left:29px}
  .lesson-name{font-size:13.5px;font-weight:500;line-height:1.3}
  .lesson-time{font-size:10.5px;color:var(--muted);margin-top:2px}

  /* tiles */
  .tile{width:157px;height:97px;border-radius:12px;background:#fff;box-shadow:0 3px 12px rgba(0,84,170,.12)}
  .tile-icon{position:absolute;left:15px;top:15px;width:40px;height:40px;border-radius:50%;
    background:linear-gradient(135deg,#1e8fde,#0a6cc4);display:flex;align-items:center;justify-content:center}
  .tile-count{position:absolute;right:20px;top:17px;font-size:20px;font-weight:500;color:var(--blue)}
  .tile-label{position:absolute;left:15px;top:66px;font-size:11px;font-weight:600}

  .video-row{left:20px;top:641px;width:335px;height:59px;border-radius:12px;background:#fff;
    box-shadow:0 3px 12px rgba(0,84,170,.12);display:flex;align-items:center;padding:0 20px 0 16px}
  .video-label{margin-left:20px;font-size:13.5px;font-weight:600;flex:1}

  /* students */
  .section-title{left:20px;top:730px;font-size:17px;font-weight:700}
  .view-all{left:283px;top:735px;font-size:12px;font-weight:600;color:var(--blue);display:flex;align-items:center;gap:5px}
  .student{width:85px;height:99px;top:774px;border-radius:10px;background:#fff;border:1px solid #e3e8ef;
    display:flex;flex-direction:column;align-items:center;padding-top:13px}
  .student-photo{width:56px;height:56px;border-radius:50%}
  .student-name{font-size:9.5px;font-weight:600;margin-top:11px}

  /* nav */
  .nav{left:0;top:930px;width:375px;height:82px;background:var(--navy)}
  .nav-icon{top:14px}
  .fab-ring{left:148px;top:891px;width:79px;height:79px;border-radius:50%;background:#fff;
    box-shadow:0 6px 16px rgba(0,0,0,.18);display:flex;align-items:center;justify-content:center}
  .fab{width:68px;height:68px;border-radius:50%;background:linear-gradient(135deg,var(--teal-a),var(--teal-b));
    display:flex;align-items:center;justify-content:center}
  .home-indicator{left:121px;top:997px;width:134px;height:5px;border-radius:3px;background:#fff}
</style>
</head>
<body>
<main class="screen">
  <div class="abs status-time">9:41</div>
  <svg class="abs status-icons" width="64" height="12" viewBox="0 0 64 12" aria-hidden="true">
    <rect x="0" y="8" width="3" height="4" rx="1" fill="#111"/><rect x="5" y="6" width="3" height="6" rx="1" fill="#111"/>
    <rect x="10" y="3" width="3" height="9" rx="1" fill="#111"/><rect x="15" y="0" width="3" height="12" rx="1" fill="#111"/>
    <path d="M24 4a9 9 0 0 1 12 0l-1.4 1.5a7 7 0 0 0-9.2 0zM26.6 6.8a5.5 5.5 0 0 1 6.8 0L30 11z" fill="#111"/>
    <rect x="41" y="1" width="21" height="10" rx="2.5" fill="none" stroke="#111" opacity=".5"/>
    <rect x="43" y="3" width="17" height="6" rx="1.5" fill="#111"/>
  </svg>

  <header>
    <div class="abs avatar" role="img" aria-label="Coach profile photo"></div>
    <div class="abs welcome">WELCOME COACH</div>
    <div class="abs coach-name">Dorian!</div>
    <div class="abs mail-btn">
      <svg width="20" height="16" viewBox="0 0 20 16" aria-hidden="true"><rect x="1" y="1" width="18" height="14" rx="2" fill="none" stroke="#0677BA" stroke-width="2"/><path d="M2 3l8 6 8-6" fill="none" stroke="#0677BA" stroke-width="2"/></svg>
    </div>
    <div class="abs mail-badge">8</div>
  </header>

  <section class="abs today">
    <div class="abs today-date">20 APRIL 2022</div>
    <div class="abs today-title">For Today</div>
    <div class="abs view-cal">VIEW CALENDAR</div>
    <div class="abs lesson" style="top:72px">
      <div class="lesson-icon"><svg width="22" height="20" viewBox="0 0 22 20" aria-hidden="true" transform="rotate(-15)"><rect x="1" y="3" width="20" height="16" rx="3" fill="#fff"/><rect x="1" y="3" width="20" height="5" rx="2" fill="#d9f3f7"/><g fill="#1aa6d3"><circle cx="6" cy="12" r="1.3"/><circle cx="11" cy="12" r="1.3"/><circle cx="16" cy="12" r="1.3"/><circle cx="6" cy="16" r="1.3"/><circle cx="11" cy="16" r="1.3"/></g></svg></div>
      <div class="lesson-text"><div class="lesson-name">My FlatRate Lesson</div><div class="lesson-time">8:00 AM - 9:30 AM</div></div>
    </div>
    <div class="abs lesson" style="top:153px">
      <div class="lesson-icon"><svg width="22" height="20" viewBox="0 0 22 20" aria-hidden="true" transform="rotate(-15)"><rect x="1" y="3" width="20" height="16" rx="3" fill="#fff"/><rect x="1" y="3" width="20" height="5" rx="2" fill="#d9f3f7"/><g fill="#1aa6d3"><circle cx="6" cy="12" r="1.3"/><circle cx="11" cy="12" r="1.3"/><circle cx="16" cy="12" r="1.3"/><circle cx="6" cy="16" r="1.3"/><circle cx="11" cy="16" r="1.3"/></g></svg></div>
      <div class="lesson-text"><div class="lesson-name">Driving Course</div><div class="lesson-time">9:30 AM - 11:00 AM</div></div>
    </div>
  </section>

  <section>
    <div class="abs tile" style="left:20px;top:407px">
      <div class="tile-icon"><svg width="22" height="18" viewBox="0 0 22 18" aria-hidden="true"><path d="M11 3C8 1 4 1 1 2v14c3-1 7-1 10 1 3-2 7-2 10-1V2c-3-1-7-1-10 1zM11 3v14" fill="none" stroke="#fff" stroke-width="1.8" stroke-linejoin="round"/></svg></div>
      <div class="tile-count">12</div><div class="tile-label">Online Lessons</div>
    </div>
    <div class="abs tile" style="left:198px;top:407px">
      <div class="tile-icon"><svg width="20" height="20" viewBox="0 0 20 20" aria-hidden="true"><path d="M10 1l8 4.5v9L10 19l-8-4.5v-9zM2 5.5l8 4.5 8-4.5M10 10v9" fill="none" stroke="#fff" stroke-width="1.8" stroke-linejoin="round"/></svg></div>
      <div class="tile-count">8</div><div class="tile-label">My Products</div>
    </div>
    <div class="abs tile" style="left:20px;top:524px">
      <div class="tile-icon"><svg width="20" height="20" viewBox="0 0 20 20" aria-hidden="true"><rect x="2" y="7" width="16" height="4" fill="none" stroke="#fff" stroke-width="1.8"/><rect x="3" y="11" width="14" height="8" fill="none" stroke="#fff" stroke-width="1.8"/><path d="M10 7v12M10 7C8 2 4 3 6 6M10 7c2-5 6-4 4-1" fill="none" stroke="#fff" stroke-width="1.8"/></svg></div>
      <div class="tile-count">10</div><div class="tile-label">My Offers</div>
    </div>
    <div class="abs tile" style="left:198px;top:524px">
      <div class="tile-icon" aria-hidden="true"></div>
      <div class="tile-label">Pond365</div>
    </div>
  </section>

  <div class="abs video-row">
    <svg width="28" height="28" viewBox="0 0 28 28" aria-hidden="true"><circle cx="14" cy="14" r="12" fill="none" stroke="#0677BA" stroke-width="1.8"/><path d="M9 3.5L17 17M2.5 12l14 1M8 24l7-12M25 16l-14-1M19 24.5L11 11M25.5 9L13 3" stroke="#0677BA" stroke-width="1.5" fill="none"/></svg>
    <div class="video-label">Video Editor</div>
    <svg width="8" height="12" viewBox="0 0 8 12" aria-hidden="true"><path d="M2 1l5 5-5 5" fill="none" stroke="#0677BA" stroke-width="2"/></svg>
  </div>

  <section>
    <h2 class="abs section-title">My Students</h2>
    <div class="abs view-all">VIEW ALL <svg width="7" height="11" viewBox="0 0 7 11" aria-hidden="true"><path d="M1 1l4.5 4.5L1 10" fill="none" stroke="#0677BA" stroke-width="2"/></svg></div>
    <div class="abs student" style="left:20px"><div class="student-photo" role="img" aria-label="Student photo" style="background:radial-gradient(circle,#e9c8b0,#3f8f72)"></div><div class="student-name">Maelle</div></div>
    <div class="abs student" style="left:115px"><div class="student-photo" role="img" aria-label="Student photo" style="background:radial-gradient(circle,#5a4a3c,#2f6b3a)"></div><div class="student-name">Brennan</div></div>
    <div class="abs student" style="left:210px"><div class="student-photo" role="img" aria-label="Student photo" style="background:radial-gradient(circle,#d8b89a,#9fb4c9)"></div><div class="student-name">Ysolde</div></div>
    <div class="abs student" style="left:305px"><div class="student-photo" role="img" aria-label="Student photo" style="background:radial-gradient(circle,#8a6a50,#3d5e4a)"></div><div class="student-name">Tobias</div></div>
  </section>

  <nav class="abs nav">
    <svg class="abs nav-icon" style="left:26px" width="24" height="24" viewBox="0 0 24 24" aria-hidden="true"><g fill="none" stroke="#fff" stroke-width="1.8"><rect x="2" y="2" width="20" height="7" rx="2"/><rect x="2" y="13" width="8" height="9" rx="2"/><rect x="14" y="13" width="8" height="9" rx="2"/></g></svg>
    <svg class="abs nav-icon" style="left:101px" width="24" height="22" viewBox="0 0 22 18" aria-hidden="true"><path d="M11 3C8 1 4 1 1 2v14c3-1 7-1 10 1 3-2 7-2 10-1V2c-3-1-7-1-10 1zM11 3v14" fill="none" stroke="#fff" stroke-width="1.5" stroke-linejoin="round"/></svg>
    <svg class="abs nav-icon" style="left:251px" width="24" height="24" viewBox="0 0 24 24" aria-hidden="true"><g fill="none" stroke="#fff" stroke-width="1.8" stroke-linejoin="round"><path d="M11 4H4a2 2 0 0 0-2 2v14a2 2 0 0 0 2 2h14a2 2 0 0 0 2-2v-7"/><path d="M18.5 2.5l3 3L12 15H9v-3z"/></g></svg>
    <svg class="abs nav-icon" style="left:326px" width="24" height="24" viewBox="0 0 24 24" aria-hidden="true"><g fill="none" stroke="#fff" stroke-width="1.6"><circle cx="12" cy="12" r="3.5"/><path d="M12 1.5l2 2.6 3.2-.8.6 3.2 3 1.4-1.4 3 1.4 3-3 1.4-.6 3.2-3.2-.8-2 2.6-2-2.6-3.2.8-.6-3.2-3-1.4 1.4-3-1.4-3 3-1.4.6-3.2 3.2.8z" stroke-linejoin="round"/></g></svg>
  </nav>
  <div class="abs fab-ring"><div class="fab"><svg width="34" height="30" viewBox="0 0 22 20" aria-hidden="true" transform="rotate(-15)"><rect x="1" y="3" width="20" height="16" rx="3" fill="#fff"/><rect x="1" y="3" width="20" height="5" rx="2" fill="#d9f3f7"/><g fill="#1aa6d3"><circle cx="6" cy="12" r="1.3"/><circle cx="11" cy="12" r="1.3"/><circle cx="16" cy="12" r="1.3"/><circle cx="6" cy="16" r="1.3"/><circle cx="11" cy="16" r="1.3"/></g></svg></div></div>
  <div class="abs home-indicator"></div>
</main>
</body>
</html>
```